Velvet Comet Cocoa Bar - ComettoBars.example

Create chocolate bar packaging. I would like the packaging to have a wizard hat or wizard with hat on on the packaging. Packaging should be a matte finish with a glossy Wizard hat or wizard with hat on the packaging. The background should have little wizard hats or mushrooms that are imbedded into the matte finish that reflect when you move the packaging. Colors should be Black, dark purple, purple, blue, dark blue, white.

Target Market(s)

Mushroom Consumers

Industry/Entity Type

Mushroom Chocolates

Font styles to use
Serif
Sans Serif

Colors
0054AA
0677BA
7BADD7
CADEEF
E8F1F8
0094D4
00A9DD
6FCCEA
C7EBF8
E9F6FB
A7469A
B969AE
D3A5CF
EDDBEB
F8F0F9
6B429C
8869AF
B7A5CE
E3DAEB
F3F0F8

Requirements
Must have
• Wizard Hat
Nice to have
• Reflective small mushrooms or wizard hats in the matte background
Should not have
• to many colors

```html
<!DOCTYPE html>
<html lang="en">
<head>
<meta charset="utf-8">
<title>Velvet Comet Cocoa Bar – Wrapper</title>
<link rel="stylesheet" href="https://fonts.googleapis.com/css2?family=Bungee&family=Raleway:wght@300;400&family=Ubuntu:wght@500&display=swap">
<style>
  :root {
    --stage: #f1d6f8;
    --crimp: #2a2433;
    --crimp-line: #3d3547;
    --body-top: #2a1a3c;
    --body-mid: #4a2768;
    --body-low: #241a30;
    --band: #a7469a;
    --band-dark: #8e3a83;
    --name: #dfe3ea;
    --soft-white: #d9d6e2;
    --flavour: #b969ae;
    --hat-teal: #35cbcf;
  }
  * { box-sizing: border-box; margin: 0; padding: 0; }
  html, body {
    width: 1200px; height: 840px; overflow: hidden;
    background: var(--stage);
  }
  .canvas {
    position: relative; width: 1200px; height: 840px;
    display: flex; align-items: center; justify-content: center;
  }
  .wrapper {
    position: relative; width: 420px; height: 780px;
    display: flex; flex-direction: column;
    box-shadow: 0 18px 40px rgba(90, 40, 110, 0.25);
  }
  .crimp {
    height: 38px; flex: none;
    background:
      repeating-linear-gradient(0deg, var(--crimp) 0 5px, var(--crimp-line) 5px 7px);
  }
  .crimp--bottom {
    background:
      repeating-linear-gradient(0deg, var(--band-dark) 0 5px, var(--band) 5px 7px);
  }
  .face {
    position: relative; flex: 1;
    background: radial-gradient(ellipse at 50% 40%, var(--body-mid) 0%, var(--body-top) 55%, var(--body-low) 100%);
    display: flex; flex-direction: column; align-items: center;
    overflow: hidden;
  }
  .face__pattern {
    position: absolute; inset: 0;
    background: radial-gradient(circle at 30% 30%, rgba(120, 90, 150, 0.18), transparent 60%),
                radial-gradient(circle at 70% 75%, rgba(90, 110, 150, 0.14), transparent 55%);
  }
  .brand {
    position: relative; margin-top: 70px;
    display: flex; flex-direction: column; align-items: center;
  }
  .brand__dot {
    width: 110px; height: 110px; border-radius: 50%;
    background: var(--hat-teal);
    margin-bottom: 34px;
  }
  .brand__name {
    font-family: "Raleway", sans-serif; font-weight: 400;
    font-size: 46px; letter-spacing: 4px; line-height: 1.05;
    color: var(--name); text-align: center;
  }
  .brand__line {
    margin-top: 14px;
    font-family: "Raleway", sans-serif; font-weight: 300;
    font-size: 30px; letter-spacing: 3px;
    color: var(--soft-white);
  }
  .flavour {
    position: relative; margin-top: 26px;
    font-family: "Bungee", sans-serif;
    font-size: 30px; color: var(--flavour); letter-spacing: 1px;
  }
  .variety {
    position: relative; margin-top: 6px;
    font-family: "Raleway", sans-serif; font-weight: 300;
    font-size: 30px; letter-spacing: 3px; color: var(--soft-white);
  }
  .band {
    flex: none; height: 130px;
    background: var(--band);
    display: flex; align-items: center; justify-content: center;
  }
  .band__text {
    font-family: "Ubuntu", sans-serif; font-weight: 500;
    font-size: 15px; letter-spacing: 0.5px; color: #ffffff;
  }
</style>
</head>
<body>
  <main class="canvas">
    <article class="wrapper">
      <div class="crimp crimp--top"></div>
      <section class="face">
        <div class="face__pattern" role="img" aria-label="Faint tone-on-tone pattern of small mushrooms and wizard hats"></div>
        <div class="brand">
          <span class="brand__dot"></span>
          <h1 class="brand__name">VELVET<br>COMET</h1>
          <p class="brand__line">COCOA BAR</p>
        </div>
        <p class="flavour">COOKIES &amp; CREAM</p>
        <p class="variety">ENIGMA</p>
      </section>
      <div class="band">
        <p class="band__text">3.5 GRAMS OF COMET MAGIC IN EVERY BAR.</p>
      </div>
      <div class="crimp crimp--bottom"></div>
    </article>
  </main>
</body>
</html>
```